Food Festival "Signature Cocktail" Booth Banner

Need a 3'x9'6" (36" tall x 114" wide) Outdoor Banner for a new "Signature Cocktail" booth at an outdoor food festival. Marlowe Onion Jubilee is a non profit festival and the World Record largest Garlic Festival with average of 100K attendees over 3 days. Actual drink served will vary from year to year, but banner for the booth with be reused each year so it will be non drink specific. Banner needs to catch attendee's attention both at a quick glance and from a distance outdoors to drive traffic and sales to the booth. It will be mounted above the sales window of a 10x10 Festival Booth on PVC frame (see attached pic for reference). "Signature Cocktail" is required text along with it being identified as a Marlowe Onion Jubilee booth either through use of attached logo (color can be modified) or "Marlowe Onion Jubilee" text since we also have for profit competing vendors. Banner will be full color print. Idea concepts: Neon Sign, Art Deco elegant, reclaimed wood...but open to any concepts. Festival website: https://marloweonionjubilee.example

Target Market(s)

Food Festival Attendees

Font styles to use
Decorative
Script
Other font styles liked:
• Neon, heavy weight fonts, open.

Colors

Designer to choose colors to be used in the design.

Requirements
Must have
• "Signature Cocktail" and "Marlowe Onion Jubilee" text or MOJ Logo provided, colors and layout that stands out and easily identifiable and readable from a long distance with strong text
Nice to have
• Vibrant engaging background,, ties to Garlic
Should not have
• Clip art, generic text

```html
<!DOCTYPE html>
<html lang="en">
<head>
<meta charset="utf-8">
<title>Signature Cocktail Booth Banner</title>
<link rel="stylesheet" href="https://fonts.googleapis.com/css2?family=Yellowtail&display=swap">
<style>
  :root {
    --bg-deep: #2a1320;
    --bg-mid: #6e1f4c;
    --bg-glow: #d3127f;
    --neon-pink: #f6c9dc;
    --neon-red: #e0263f;
    --neon-cream: #fff6d0;
    --neon-yellow: #f1dc72;
    --festival-orange: #ea4e36;
    --glass-pink: #f3c6da;
  }
  * { margin: 0; padding: 0; box-sizing: border-box; }
  html, body { width: 1200px; height: 379px; overflow: hidden; background: var(--bg-deep); }
  .banner {
    position: relative;
    width: 1200px;
    height: 379px;
    overflow: hidden;
    background:
      radial-gradient(ellipse 500px 250px at 610px 190px, var(--bg-glow) 0%, var(--bg-mid) 45%, transparent 100%),
      linear-gradient(180deg, #3a1629 0%, var(--bg-deep) 100%);
    font-family: "Yellowtail", "Brush Script MT", cursive;
  }
  .martini-sign {
    position: absolute;
    left: 26px;
    top: 50px;
    width: 220px;
    height: 300px;
    border-radius: 10px;
    background: radial-gradient(ellipse at 50% 35%, rgba(243, 198, 218, 0.22) 0%, rgba(243, 198, 218, 0.06) 60%, transparent 100%);
  }
  .headline { position: absolute; inset: 0; font-weight: 400; }
  .headline__signature {
    position: absolute;
    left: 290px;
    top: 58px;
    font-size: 92px;
    line-height: 1;
    color: var(--neon-pink);
    -webkit-text-stroke: 2px var(--neon-red);
    text-shadow: 0 0 8px rgba(224, 38, 63, 0.45);
    transform: rotate(-5deg);
    transform-origin: left bottom;
    white-space: nowrap;
  }
  .headline__cocktail {
    position: absolute;
    left: 182px;
    top: 168px;
    font-size: 158px;
    line-height: 1;
    color: var(--neon-cream);
    -webkit-text-stroke: 2px var(--neon-yellow);
    text-shadow:
      0 0 4px var(--neon-yellow),
      0 0 14px rgba(241, 220, 114, 0.7),
      0 0 28px rgba(241, 220, 114, 0.35);
    transform: rotate(-5deg);
    transform-origin: left bottom;
    white-space: nowrap;
  }
  .festival-mark {
    position: absolute;
    left: 910px;
    top: 118px;
    width: 230px;
    text-align: center;
  }
  .festival-mark__name {
    font-size: 46px;
    line-height: 1.05;
    color: var(--festival-orange);
  }
</style>
</head>
<body>
  <main class="banner">
    <div class="martini-sign" role="img" aria-label="Pink neon martini glass with a green neon olive on a pick"></div>

    <h1 class="headline">
      <span class="headline__signature">Signature</span>
      <span class="headline__cocktail">Cocktail</span>
    </h1>

    <div class="festival-mark">
      <p class="festival-mark__name">Marlowe<br>Onion<br>Jubilee</p>
    </div>
  </main>
</body>
</html>
```